Existing Website Requiring new Pages

I have an existing word press website that was built using elementor.
Website: www.tallowcreekcare.com.au
I require the Vacancies page (https://www.tallowcreekcare.com.au/vacancies/) to be modified to display our new properties along with minor tweaks to how the information is presented.
The vacancies to be displayed are the exactly the same as those that are located on the homepage of QMR website (https://qmr.org.au/)
The new pages that link off the Vacancies tab will require custom design.
There are roughly 8 pages/properties to be incorporated. i wish for the design to be very similar to that displayed in the following link; https://www.pelunor.com.au/vacancies/dunmarra
Along with this the back end has not been updated for the last 3 years so it also requires some maintenance.
Website is in the disability industry and the custom pages will display information relative to Property Vacancies.
I have attached a ZIP file with some design guides, the information for each of the properties (which will need to be modified to show our business name Tallowcreek Care) and the example of how it is to look based off the Pelunor website.
If you guys have any suggestions or ideas on how to make this more presentable or possible i'm open to your ideas.
Target Market(s)
People looking for SDA properties custom built for people with a disability
Industry/Entity Type
Disability
Coding
Coded - Design and coding required
Number of Pages Required
5+ page
Look and feel

```html
<!DOCTYPE html>
<html lang="en">
<head>
<meta charset="utf-8">
<title>Vacancies | Tallowcreek Care</title>
<link href="https://fonts.googleapis.com/css2?family=Montserrat:wght@400;500;600;700;800&display=swap" rel="stylesheet">
<style>
:root{
  --orange:#f8b446;
  --orange-soft:#f7bd5a;
  --teal:#34c7b4;
  --ink:#1c1c1c;
  --muted:#8d8d8d;
  --line:#e4e4e4;
  --field:#eeeeee;
  --footer:#f6f6f6;
  --bar:#262626;
  --tag:#3a3a3a;
  --featured:#3fe0b2;
}
*{box-sizing:border-box;margin:0;padding:0}
html,body{width:1200px;height:3275px;overflow:hidden}
body{position:relative;font-family:'Montserrat',sans-serif;color:var(--ink);background:#fff}
.abs{position:absolute}

/* header */
.site-header{left:0;top:0;width:1200px;height:114px;background:#fff}
.brand{left:89px;top:30px;display:flex;align-items:center;gap:8px}
.brand-dot{width:22px;height:22px;border-radius:50%;background:#e56bb5}
.brand-name{font-size:14px;font-weight:600;color:#3d3d3d;line-height:1.2;letter-spacing:.5px}
.main-nav{left:494px;top:52px;display:flex;gap:19px;font-size:12px;font-weight:600}
.main-nav a{color:var(--ink);text-decoration:none}
.main-nav a.active{color:var(--orange)}
.btn-contact{left:968px;top:38px;width:144px;height:42px;background:var(--orange);border-radius:3px;font-size:14px;font-weight:600;display:flex;align-items:center;justify-content:center;color:var(--ink)}

/* hero */
.hero-photo{left:0;top:114px;width:1200px;height:561px;background:linear-gradient(120deg,#b08a6a 0%,#8c7b6e 35%,#a7a39d 60%,#7e7a74 100%)}
.hero-overlay{left:0;top:114px}
.hero-title{left:91px;top:338px;font-size:60px;font-weight:800;letter-spacing:-1px;color:#111}

/* filter */
.filter{left:158px;top:596px;width:884px;height:156px;background:#fff;box-shadow:0 6px 24px rgba(0,0,0,.1)}
.filter-label{top:38px;font-size:14px;font-weight:600}
.filter-select{top:71px;width:229px;height:46px;background:var(--field);font-size:12px;font-weight:500;color:#555;display:flex;align-items:center;justify-content:space-between;padding:0 17px}
.btn-go{left:789px;top:71px;width:75px;height:46px;background:var(--orange);font-size:14px;font-weight:600;display:flex;align-items:center;justify-content:center}

/* map */
.map{left:139px;top:843px;width:922px;height:436px;background:linear-gradient(90deg,#d8ead8 0%,#e4eee0 55%,#cfe6ec 75%,#9fd4ea 100%)}

/* properties */
.eyebrow{left:0;top:1366px;width:1200px;text-align:center;font-size:13px;font-weight:600;color:var(--teal);letter-spacing:.5px}
.section-title{left:0;top:1398px;width:1200px;text-align:center;font-size:32px;font-weight:600;line-height:36px}
.title-rule{left:545px;top:1483px;width:110px;height:3px;background:var(--teal)}

.card{width:317px;height:386px;background:#fff;box-shadow:0 4px 18px rgba(0,0,0,.07)}
.card-media{position:relative;height:238px}
.tags{position:absolute;top:18px;left:18px;right:12px;display:flex;gap:6px;justify-content:space-between}
.tags.end{justify-content:flex-end}
.tag{font-size:8.5px;font-weight:700;color:#fff;background:var(--tag);padding:3px 11px;border-radius:2px;white-space:nowrap}
.tag.featured{background:var(--featured);color:#1d4a3f}
.dots{position:absolute;bottom:20px;left:50%;transform:translateX(-50%);display:flex;gap:4px}
.dots i{width:7px;height:7px;border-radius:50%;background:rgba(255,255,255,.7)}
.dots i:nth-child(2){background:#fff}
.expand{position:absolute;right:12px;bottom:12px;width:36px;height:32px;background:#1f1f1f;display:flex;align-items:center;justify-content:center;border-radius:2px}
.card-body{padding:14px 18px 0}
.card-title{font-size:14px;font-weight:600;text-transform:uppercase;margin-top:6px}
.card-loc{font-size:12px;color:#555;margin-top:6px;display:flex;align-items:center;gap:4px}
.card-feat{font-size:9.5px;font-weight:500;color:#555;margin-top:16px;height:28px;line-height:14px;text-transform:uppercase}
.btn-view{display:inline-block;margin-top:10px;background:var(--orange);font-size:10px;font-weight:600;padding:6px 14px;border-radius:2px}

/* footer */
.site-footer{left:0;top:2888px;width:1200px;height:315px;background:var(--footer)}
.footer-brand{left:89px;top:2990px;display:flex;align-items:center;gap:10px}
.footer-brand .brand-dot{width:34px;height:34px}
.footer-brand .brand-name{font-size:22px}
.contact-list{left:89px;top:3097px;font-size:13px;color:#888;line-height:24px}
.contact-list li{list-style:none;display:flex;align-items:center;gap:9px}
.social{left:516px;top:2944px;display:flex;flex-direction:column;gap:8px}
.social span{width:34px;height:34px;border-radius:50%;background:#1f1f1f}
.social span:first-child{background:#6a2c70}
.social span:nth-child(2),.social span:nth-child(4){background:#1f5b97}
.foot-col{top:2934px;width:236px}
.foot-col h4{font-size:14px;font-weight:500;border-left:3px solid var(--orange);padding-left:14px;letter-spacing:.5px;margin-bottom:12px}
.foot-col a{display:block;font-size:13px;color:#9a9a9a;line-height:23px;padding:6px 0;border-bottom:1px solid var(--line);text-decoration:none}
.copyright-bar{left:0;top:3203px;width:1200px;height:72px;background:var(--bar)}
.copyright{left:0;top:3230px;width:1200px;text-align:center;font-size:10px;color:#aaa}
.to-top{left:1129px;top:3218px;width:34px;height:36px;background:#111;display:flex;align-items:center;justify-content:center}
</style>
</head>
<body>

<header class="site-header abs">
  <div class="brand abs"><span class="brand-dot"></span><span class="brand-name">TALLOWCREEK<br>CARE</span></div>
  <nav class="main-nav abs">
    <a href="#">HOME</a><a href="#">ABOUT US</a><a href="#" class="active">WHAT WE DO ⌄</a><a href="#">REFERRALS</a><a href="#">FEEDBACK</a>
  </nav>
  <div class="btn-contact abs">CONTACT US</div>
</header>

<div class="hero-photo abs" role="img" aria-label="Woman in a wheelchair working at a laptop at a wooden table in a brick-walled kitchen"></div>
<svg class="hero-overlay abs" width="1200" height="561" viewBox="0 0 1200 561">
  <polygon points="0,0 381,0 623,561 0,561" fill="#f8b446" opacity=".94"/>
</svg>
<h1 class="hero-title abs">VACANCIES</h1>

<form class="filter abs">
  <div class="filter-label abs" style="left:20px">CURRENT OR FUTURE</div>
  <div class="filter-label abs" style="left:278px">DESIGN CATEGORY</div>
  <div class="filter-label abs" style="left:545px">LOCATION</div>
  <div class="filter-select abs" style="left:20px">BOTH <span>⇕</span></div>
  <div class="filter-select abs" style="left:278px">ALL CATEGORIES <span>⇕</span></div>
  <div class="filter-select abs" style="left:545px">ALL SUBURBS <span>⇕</span></div>
  <div class="btn-go abs">GO</div>
</form>

<div class="map abs" role="img" aria-label="Map of Greater Western Sydney with the service area highlighted"></div>

<div class="eyebrow abs">PROPERTIES</div>
<h2 class="section-title abs">VIEW OUR SDA VACANCIES AND<br>HOMES BEING BUILT</h2>
<div class="title-rule abs"></div>

<!-- row 1 -->
<article class="card abs" style="left:95px;top:1524px">
  <div class="card-media" role="img" aria-label="Two-storey brick townhouse with balconies" style="background:linear-gradient(180deg,#c9cfd6,#9c8a72 60%,#6d6a62)">
    <div class="tags"><span class="tag featured">FEATURED</span><span class="tag">ALL MOST - APPLY NOW</span><span class="tag">APPLY NOW</span></div>
    <div class="dots"><i></i><i></i><i></i></div>
    <div class="expand"><svg width="16" height="16" viewBox="0 0 16 16" fill="none" stroke="#fff" stroke-width="1.6"><path d="M2 14L14 2M9 2h5v5M2 9v5h5"/></svg></div>
  </div>
  <div class="card-body">
    <h3 class="card-title">SDA in Greystanes</h3>
    <div class="card-loc"><svg width="9" height="12" viewBox="0 0 9 12"><path d="M4.5 0A4.5 4.5 0 0 0 0 4.5C0 8 4.5 12 4.5 12S9 8 9 4.5A4.5 4.5 0 0 0 4.5 0z" fill="#f8b446"/></svg>Greystanes</div>
    <div class="card-feat">Fully Accessible, High Physical Support</div>
    <span class="btn-view">VIEW DETAILS</span>
  </div>
</article>
<article class="card abs" style="left:441px;top:1524px">
  <div class="card-media" role="img" aria-label="Brick duplex with a garage and driveway" style="background:linear-gradient(180deg,#b9c6d3,#8a6a58 55%,#5f5a55)">
    <div class="tags"><span class="tag featured">FEATURED</span><span class="tag">AVAILABLE NOW</span><span class="tag">CURRENT VACANCY</span></div>
    <div class="dots"><i></i><i></i><i></i></div>
    <div class="expand"><svg width="16" height="16" viewBox="0 0 16 16" fill="none" stroke="#fff" stroke-width="1.6"><path d="M2 14L14 2M9 2h5v5M2 9v5h5"/></svg></div>
  </div>
  <div class="card-body">
    <h3 class="card-title">SDA in Jordan Springs</h3>
    <div class="card-loc"><svg width="9" height="12" viewBox="0 0 9 12"><path d="M4.5 0A4.5 4.5 0 0 0 0 4.5C0 8 4.5 12 4.5 12S9 8 9 4.5A4.5 4.5 0 0 0 4.5 0z" fill="#f8b446"/></svg>Jordan Springs</div>
    <div class="card-feat">Fully Accessible, Improved Liveability</div>
    <span class="btn-view">VIEW DETAILS</span>
  </div>
</article>
<article class="card abs" style="left:787px;top:1524px">
  <div class="card-media" role="img" aria-label="Modern two-storey house with balcony" style="background:linear-gradient(180deg,#d5d8dc,#8a7c70 55%,#6b6a66)">
    <div class="tags"><span class="tag featured">FEATURED</span><span class="tag">AVAILABLE NOW</span><span class="tag">CURRENT VACANCY</span></div>
    <div class="dots"><i></i><i></i><i></i></div>
    <div class="expand"><svg width="16" height="16" viewBox="0 0 16 16" fill="none" stroke="#fff" stroke-width="1.6"><path d="M2 14L14 2M9 2h5v5M2 9v5h5"/></svg></div>
  </div>
  <div class="card-body">
    <h3 class="card-title">SDA in Werrington</h3>
    <div class="card-loc"><svg width="9" height="12" viewBox="0 0 9 12"><path d="M4.5 0A4.5 4.5 0 0 0 0 4.5C0 8 4.5 12 4.5 12S9 8 9 4.5A4.5 4.5 0 0 0 4.5 0z" fill="#f8b446"/></svg>Werrington</div>
    <div class="card-feat">Fully Accessible, Improved Liveability</div>
    <span class="btn-view">VIEW DETAILS</span>
  </div>
</article>

<!-- row 2 -->
<article class="card abs" style="left:95px;top:1966px">
  <div class="card-media" role="img" aria-label="Single-storey dark brick villas" style="background:linear-gradient(180deg,#4d6584,#7a7a7c 50%,#555)">
    <div class="tags"><span class="tag featured">FEATURED</span><span class="tag">AVAILABLE NOW</span><span class="tag">NEW CONSTRUCTION</span></div>
    <div class="dots"><i></i><i></i><i></i></div>
    <div class="expand"><svg width="16" height="16" viewBox="0 0 16 16" fill="none" stroke="#fff" stroke-width="1.6"><path d="M2 14L14 2M9 2h5v5M2 9v5h5"/></svg></div>
  </div>
  <div class="card-body">
    <h3 class="card-title">SDA Villas in Wentworthville</h3>
    <div class="card-loc"><svg width="9" height="12" viewBox="0 0 9 12"><path d="M4.5 0A4.5 4.5 0 0 0 0 4.5C0 8 4.5 12 4.5 12S9 8 9 4.5A4.5 4.5 0 0 0 4.5 0z" fill="#f8b446"/></svg>Wentworthville</div>
    <div class="card-feat">Fully Accessible, High Physical Support, Improved Liveability</div>
    <span class="btn-view">VIEW DETAILS</span>
  </div>
</article>
<article class="card abs" style="left:441px;top:1966px">
  <div class="card-media" role="img" aria-label="Two-storey brick home with front garden" style="background:linear-gradient(180deg,#4b6688,#7b6a5e 55%,#5d6a52)">
    <div class="tags end"><span class="tag">CURRENT VACANCY</span><span class="tag">APPLY NOW</span></div>
    <div class="dots"><i></i><i></i><i></i></div>
    <div class="expand"><svg width="16" height="16" viewBox="0 0 16 16" fill="none" stroke="#fff" stroke-width="1.6"><path d="M2 14L14 2M9 2h5v5M2 9v5h5"/></svg></div>
  </div>
  <div class="card-body">
    <h3 class="card-title">SDA in West Pennant Hills</h3>
    <div class="card-loc"><svg width="9" height="12" viewBox="0 0 9 12"><path d="M4.5 0A4.5 4.5 0 0 0 0 4.5C0 8 4.5 12 4.5 12S9 8 9 4.5A4.5 4.5 0 0 0 4.5 0z" fill="#f8b446"/></svg>West Pennant Hills</div>
    <div class="card-feat">High Physical Support</div>
    <span class="btn-view">VIEW DETAILS</span>
  </div>
</article>
<article class="card abs" style="left:787px;top:1966px">
  <div class="card-media" role="img" aria-label="New two-storey rendered home" style="background:linear-gradient(180deg,#3e5f8f,#8d9096 55%,#656565)">
    <div class="tags end"><span class="tag">NEW CONSTRUCTION</span><span class="tag">APPLY NOW</span></div>
    <div class="dots"><i></i><i></i><i></i></div>
    <div class="expand"><svg width="16" height="16" viewBox="0 0 16 16" fill="none" stroke="#fff" stroke-width="1.6"><path d="M2 14L14 2M9 2h5v5M2 9v5h5"/></svg></div>
  </div>
  <div class="card-body">
    <h3 class="card-title">SDA in Guildford West</h3>
    <div class="card-loc"><svg width="9" height="12" viewBox="0 0 9 12"><path d="M4.5 0A4.5 4.5 0 0 0 0 4.5C0 8 4.5 12 4.5 12S9 8 9 4.5A4.5 4.5 0 0 0 4.5 0z" fill="#f8b446"/></svg>Guildford West</div>
    <div class="card-feat">Fully Accessible, High Physical Support</div>
    <span class="btn-view">VIEW DETAILS</span>
  </div>
</article>

<!-- row 3 -->
<article class="card abs" style="left:95px;top:2409px">
  <div class="card-media" role="img" aria-label="Accessible kitchen with green tiled splashback" style="background:linear-gradient(180deg,#e8e8e6,#b8b6b0 60%,#a08a6c)">
    <div class="tags end"><span class="tag">REGISTER YOU INTEREST TODAY</span><span class="tag">APPLY NOW</span></div>
    <div class="dots"><i></i><i></i><i></i></div>
    <div class="expand"><svg width="16" height="16" viewBox="0 0 16 16" fill="none" stroke="#fff" stroke-width="1.6"><path d="M2 14L14 2M9 2h5v5M2 9v5h5"/></svg></div>
  </div>
  <div class="card-body">
    <h3 class="card-title">SDA in Austral</h3>
    <div class="card-loc"><svg width="9" height="12" viewBox="0 0 9 12"><path d="M4.5 0A4.5 4.5 0 0 0 0 4.5C0 8 4.5 12 4.5 12S9 8 9 4.5A4.5 4.5 0 0 0 4.5 0z" fill="#f8b446"/></svg>Austral</div>
    <div class="card-feat">Fully Accessible, High Physical Support, Robust</div>
    <span class="btn-view">VIEW DETAILS</span>
  </div>
</article>
<article class="card abs" style="left:441px;top:2409px">
  <div class="card-media" role="img" aria-label="Row of red brick townhouses" style="background:linear-gradient(180deg,#6f8db4,#8b5a48 55%,#6a625a)">
    <div class="tags end"><span class="tag">AVAILABLE NOW</span><span class="tag">CURRENT VACANCY</span></div>
    <div class="dots"><i></i><i></i><i></i></div>
    <div class="expand"><svg width="16" height="16" viewBox="0 0 16 16" fill="none" stroke="#fff" stroke-width="1.6"><path d="M2 14L14 2M9 2h5v5M2 9v5h5"/></svg></div>
  </div>
  <div class="card-body">
    <h3 class="card-title">SDA in Merrylands</h3>
    <div class="card-loc"><svg width="9" height="12" viewBox="0 0 9 12"><path d="M4.5 0A4.5 4.5 0 0 0 0 4.5C0 8 4.5 12 4.5 12S9 8 9 4.5A4.5 4.5 0 0 0 4.5 0z" fill="#f8b446"/></svg>Merrylands</div>
    <div class="card-feat">Fully Accessible, High Physical Support</div>
    <span class="btn-view">VIEW DETAILS</span>
  </div>
</article>
<article class="card abs" style="left:787px;top:2409px">
  <div class="card-media" role="img" aria-label="Single-storey home with dark brick front" style="background:linear-gradient(180deg,#a9b5c2,#6f6f72 55%,#4f5a48)">
    <div class="tags end"><span class="tag">EXPRESSION OF INTEREST</span><span class="tag">APPLY NOW</span></div>
    <div class="dots"><i></i><i></i><i></i></div>
    <div class="expand"><svg width="16" height="16" viewBox="0 0 16 16" fill="none" stroke="#fff" stroke-width="1.6"><path d="M2 14L14 2M9 2h5v5M2 9v5h5"/></svg></div>
  </div>
  <div class="card-body">
    <h3 class="card-title">SDA in Blacktown – 1 Bedroom…</h3>
    <div class="card-loc"><svg width="9" height="12" viewBox="0 0 9 12"><path d="M4.5 0A4.5 4.5 0 0 0 0 4.5C0 8 4.5 12 4.5 12S9 8 9 4.5A4.5 4.5 0 0 0 4.5 0z" fill="#f8b446"/></svg>Blacktown</div>
    <div class="card-feat">High Physical Support</div>
    <span class="btn-view">VIEW DETAILS</span>
  </div>
</article>

<footer class="site-footer abs"></footer>
<div class="footer-brand abs"><span class="brand-dot"></span><span class="brand-name">TALLOWCREEK CARE</span></div>
<ul class="contact-list abs">
  <li><svg width="14" height="11" viewBox="0 0 14 11" fill="none" stroke="#e0558f" stroke-width="1.3"><rect x=".7" y=".7" width="12.6" height="9.6"/><path d="M.7 .7L7 6l6.3-5.3"/></svg>Email: info@tallowcreekcare.com.au</li>
  <li><svg width="13" height="13" viewBox="0 0 13 13"><path d="M2.5 0l2.3 2.8-1.4 1.6a8 8 0 0 0 5.2 5.2l1.6-1.4L13 10.5 11.5 13C5 13 0 8 0 1.5z" fill="#e0558f"/></svg>Phone: +61 0412 583 206</li>
  <li><svg width="13" height="13" viewBox="0 0 13 13" fill="none" stroke="#e0558f" stroke-width="1.3"><circle cx="6.5" cy="6.5" r="5.8"/><path d="M6.5 3v3.5l2.5 1.5"/></svg>Operating Hours: 9AM To 5PM Monday - Friday</li>
</ul>
<div class="social abs"><span></span><span></span><span></span><span></span></div>
<nav class="foot-col abs" style="left:613px">
  <h4>ACCOMMODATION</h4>
  <a href="#">Supported Independent Living (SIL)</a>
  <a href="#">Specialist Disability Accommodation (SDA)</a>
  <a href="#">Short term Accommodation (Respite)</a>
  <a href="#">Vacancies</a>
</nav>
<nav class="foot-col abs" style="left:874px">
  <h4>WHAT WE DO</h4>
  <a href="#">In Home Care</a>
  <a href="#">Social &amp; Community Services</a>
  <a href="#">Therapeutic Supports</a>
  <a href="#">Support Coordination</a>
  <a href="#">Home Modifications</a>
</nav>
<div class="copyright-bar abs"></div>
<div class="copyright abs">© Copyright 2021 | Tallowcreek Care | All Rights Reserved.</div>
<div class="to-top abs"><svg width="10" height="7" viewBox="0 0 10 7"><path d="M5 0l5 7H0z" fill="#fff"/></svg></div>

</body>
</html>
```